Business cards and stationary for seafood company in Iceland
From Calm and Lofty Fjordland
Business cards and stationary for seafood company in Iceland - Food
Creative Brief
Simple
VEXA-Fjord ehf.
President
Hvalsteinsgata 17 108 Reykjavik Iceland
tmelvar58@brindlemail.com
Use all your creative words to express my new logo which just got from this website.
korvadesigns korvadesigns
vexafjord vexafjord
#114 is perfect! thanks a lot!
I couldn't find AI or EPS format from the files I downloaded from your web. I need help on that! Thanks.
Oh, Sorry, I am getting the LOGO now on this web. I don't know I should get the logo first and then ask for card design later. It seemed that I made a mistake by launch this too early. Any comments on this situation? Thanks!
mellowfin mellowfin
Hi , can you please attach your existing logo . Thanks

```html
<!DOCTYPE html>
<html lang="en">
<head>
<meta charset="utf-8">
<title>VEXA-Fjord business cards</title>
<link href="https://fonts.googleapis.com/css2?family=Open+Sans:wght@400;600;700&display=swap" rel="stylesheet">
<style>
  :root {
    --bg: #e4e5e7;
    --blue-light: #2ea3e6;
    --blue: #1482cc;
    --blue-dark: #0a5fa6;
    --orange: #f5961e;
    --navy: #1c3f78;
    --ink: #4a4f57;
    --white: #ffffff;
  }
  * { margin: 0; padding: 0; box-sizing: border-box; }
  html, body { width: 1200px; height: 987px; overflow: hidden; }
  body {
    background: var(--bg);
    font-family: "Open Sans", Arial, sans-serif;
    position: relative;
  }
  .card {
    position: absolute;
    width: 640px;
    height: 366px;
    border-radius: 26px;
    overflow: hidden;
    box-shadow: 0 14px 30px rgba(0,0,0,0.18);
  }
  .card-back {
    left: 430px; top: 70px;
    background: radial-gradient(ellipse at 45% 40%, var(--blue-light) 0%, var(--blue) 55%, var(--blue-dark) 100%);
  }
  .card-front { left: 150px; top: 500px; background: var(--white); }

  .brand {
    position: absolute;
    display: flex; align-items: center; gap: 12px;
    font-weight: 700; letter-spacing: 1px;
  }
  .brand-dot { border-radius: 50%; flex: none; }
  .card-back .brand { left: 0; right: 0; top: 150px; justify-content: center; color: var(--white); font-size: 38px; }
  .card-back .brand-dot { width: 40px; height: 40px; background: var(--white); }
  .website {
    position: absolute; left: 0; right: 0; top: 272px;
    text-align: center; color: var(--white); font-size: 15px;
  }

  .card-front .brand { left: 50px; top: 120px; color: var(--navy); font-size: 34px; }
  .card-front .brand-dot { width: 34px; height: 34px; background: var(--blue); }
  .swoosh { position: absolute; left: 0; bottom: 0; width: 640px; height: 366px; }

  .person { position: absolute; left: 392px; top: 96px; }
  .person-name { color: var(--blue); font-size: 17px; font-weight: 600; }
  .person-title { color: var(--ink); font-size: 13px; font-style: italic; }
  .contact {
    position: absolute; left: 392px; top: 150px;
    border-left: 1px solid #9aa3ad; padding-left: 12px;
    list-style: none;
  }
  .contact li {
    display: flex; align-items: center; gap: 8px;
    font-size: 12.5px; color: var(--ink); line-height: 21px;
  }
  .contact svg { width: 12px; height: 12px; flex: none; fill: var(--blue); }
</style>
</head>
<body>

<section class="card card-back" aria-label="Card back">
  <div class="brand"><span class="brand-dot"></span>VEXA-Fjord</div>
  <p class="website">www.vexafjord-sample.is</p>
</section>

<section class="card card-front" aria-label="Card front">
  <svg class="swoosh" viewBox="0 0 640 366" preserveAspectRatio="none" aria-hidden="true">
    <path d="M0 210 C120 250 200 330 380 366 L0 366 Z" fill="var(--orange)"/>
    <path d="M0 232 C140 262 230 340 420 366 L0 366 Z" fill="var(--white)"/>
    <path d="M0 248 C150 280 250 350 470 366 L0 366 Z" fill="var(--blue)"/>
    <path d="M300 366 C450 350 560 320 640 280 L640 300 C560 340 470 362 360 366 Z" fill="var(--orange)"/>
    <path d="M120 366 C350 370 520 340 640 300 L640 366 Z" fill="var(--blue-dark)" opacity="0.9"/>
  </svg>

  <div class="brand"><span class="brand-dot"></span>VEXA-Fjord</div>

  <div class="person">
    <p class="person-name">Arna Sample</p>
    <p class="person-title">President</p>
  </div>

  <ul class="contact">
    <li><svg viewBox="0 0 12 12"><path d="M6 0a4 4 0 0 0-4 4c0 3 4 8 4 8s4-5 4-8a4 4 0 0 0-4-4zm0 5.5A1.5 1.5 0 1 1 6 2.5a1.5 1.5 0 0 1 0 3z"/></svg>Hvalsteinsgata 17</li>
    <li><svg viewBox="0 0 12 12"><circle cx="6" cy="6" r="2"/></svg>108 Reykjavik Iceland</li>
    <li><svg viewBox="0 0 12 12"><path d="M2.5 0l2 3-1.2 1.3a7 7 0 0 0 4.4 4.4L9 7.5l3 2-1.5 2.5C5 12 0 7 0 1.5z"/></svg>+354 555 0142</li>
    <li><svg viewBox="0 0 12 12"><path d="M2.5 0l2 3-1.2 1.3a7 7 0 0 0 4.4 4.4L9 7.5l3 2-1.5 2.5C5 12 0 7 0 1.5z"/></svg>+354 555 0178</li>
    <li><svg viewBox="0 0 12 12"><path d="M0 2h12v8H0zM0 2l6 4.5L12 2" fill="none" stroke="var(--blue)" stroke-width="1.4"/></svg>tmelvar58@brindlemail.com</li>
    <li><svg viewBox="0 0 12 12"><circle cx="6" cy="6" r="5" fill="none" stroke="var(--blue)" stroke-width="1.4"/><path d="M1 6h10M6 1c-2 3-2 7 0 10M6 1c2 3 2 7 0 10" fill="none" stroke="var(--blue)" stroke-width="1"/></svg>www.vexafjord-sample.is</li>
  </ul>
</section>

</body>
</html>
```